Information about this product:

1) Highlights

-Enhances UV protection
-Gradually builds UV tolerance
-Promotes a more youthful appearance
-Provides antioxidant benefits

2) Marketing

Boost your regular sun protection with MARIVO.

MARIVO offers sun protection and anti-aging benefits with a powerful blend of antioxidants. These daily supplements help defend your skin from the inside out. This formula helps gradually build up your body’s natural defense against the sun’s rays. Take MARIVO pill whenever you feel like sunscreen isn’t enough or once a day to maintain youthful skin.

Tarnvexil helps protect skin against sun-related damage
Vitamin C and pomegranate extract reduce free radical damage
Daily use promotes younger-looking skin
Each capsule is gluten-free and vegetarian
Protect your skin against photoaging and other sun damage with MARIVO - Sun Protection Pills.

3) Ingredients

Polypodium Leucotomos Extract —> 240mg
Brelundix® Methyl-Sulfonyl-Methane (MSM) —> 200mg
Grape Extract (Rich in Resveratrol and Vitamin E) —> 150mg
Pomegranate Extract (Punica Granatum) —> 125mg
Quistradex (French Maritime Pine Bark Extract) —> 35.5mg
Lutein (Contains Zeaxanthin 300mcg) —> 7.5mg
Organic Carrot Powder - Contains 3,500 IU of Vitamin A (as beta-carotene) —> 13 mg (70% Daily value)

I just started this project last month and I need a label for this product.

It is attached some labels from the competitors.

I have thought in some names to this Product but I didn't set one yet. I have 2 names and would like to know what you guys think about: Marivo and Kel4.

I would love some suggestions.

This product will be sold in Brazil first, and next summer here in USA.

Any question please, let me know!

Looking forward to work with you!

Thanks

Colette

Target Market(s)

Women between 25 to 70 years old. People who had skin cancer and need extra protection.

Industry/Entity Type

Supplement

Font styles to use
Serif
Script

Requirements
Must have
• As I can't let explicit the information about sunblock in the Label, because of the rules of Brazil, the label of this product must try to show the client what it's the purpose of this product without words.
• I need the label in Illustrator format.
Nice to have
• This product is an extra protection for the sun! It comes to protect the second layer of your skin, so the main point of it it is to prevent from skin cancer, specially.
• It also has anti-aging products (resveratrol and MSM) so I think it is nice to point this in the label.
• I don't like a lot of information, I would prefer something clean!
• you can apply something metallic or different in the label if you want too.
• I like the bottle from harbor's wellspry (Skin, hair and nails). It is white and the size is perfect.
• I like the sunset and sunrise colors, but as I don't understand about design I would prefer let you choose the perfect color for this kind of product.
Should not have
• Medicament information. We can't write that we are going to save people from disease or something else.

```html
<!DOCTYPE html>
<html lang="en">
<head>
<meta charset="utf-8">
<title>Kel4 – Daily Use Antioxidant Formula Label</title>
<link rel="stylesheet" href="https://fonts.googleapis.com/css2?family=Signika:wght@400;600;700&display=swap">
<style>
  :root{
    --page:#f4f4f4;
    --ink:#1d1d1f;
    --brown:#3a2415;
    --white:#ffffff;
    --sky-gold:#f6c445;
    --sky-orange:#ef7d2a;
    --sky-red:#d9542a;
    --sea-light:#5fb3e6;
    --sea-mid:#2c86d2;
    --sea-deep:#1b5fae;
    --cool-violet:#8f8fc6;
    --pill:#d9d9dc;
    --rule:#111111;
  }
  *{box-sizing:border-box;margin:0;padding:0}
  html,body{width:1200px;height:1200px;overflow:hidden;background:var(--page)}
  body{font-family:"Signika",sans-serif;color:var(--ink);position:relative}

  .label{position:absolute;left:50px;width:1100px;height:520px;overflow:hidden;border-radius:6px;box-shadow:0 2px 10px rgba(0,0,0,.12)}
  .label--warm{top:50px}
  .label--cool{top:630px}

  .label__scene{position:absolute;inset:0}
  .label--warm .label__scene{background:linear-gradient(180deg,var(--sky-gold) 0%,#f3a43a 22%,var(--sky-orange) 42%,var(--sky-red) 55%,#e9b77a 62%,var(--sea-light) 68%,var(--sea-mid) 82%,var(--sea-deep) 100%)}
  .label--cool .label__scene{background:linear-gradient(180deg,#cfd2ea 0%,#f1e6c9 18%,#f2b25a 36%,#e3713a 52%,#c9b6c6 61%,var(--sea-light) 68%,var(--sea-mid) 82%,var(--sea-deep) 100%)}
  .label--cool .label__scene::after{content:"";position:absolute;inset:0;background:linear-gradient(90deg,rgba(143,143,198,.55) 0%,rgba(143,143,198,0) 22%,rgba(143,143,198,0) 78%,rgba(143,143,198,.55) 100%)}

  .panel-story{position:absolute;left:40px;top:70px;width:200px;font-size:13px;line-height:1.5;color:var(--ink)}

  .panel-front{position:absolute;left:300px;top:0;width:500px;height:520px}
  .kind{position:absolute;left:0;top:40px;font-weight:700;font-size:21px;letter-spacing:1.5px;line-height:1.4;color:var(--ink)}
  .brand{position:absolute;left:-6px;top:125px;display:flex;align-items:center;gap:14px}
  .brand__name{font-weight:700;font-size:112px;line-height:1;color:var(--white)}
  .brand__mark{width:22px;height:22px;border-radius:50%;background:var(--white)}
  .tagline{position:absolute;left:0;top:248px;font-weight:600;font-size:22px;line-height:1.35;color:var(--brown)}
  .highlights{position:absolute;left:0;top:322px;list-style:none;font-size:15px;line-height:1.35;color:var(--white)}
  .highlights li::before{content:"•";margin-right:5px}
  .formula{position:absolute;left:0;top:414px;font-weight:700;font-size:21px;letter-spacing:1.5px;line-height:1.35;color:var(--ink)}
  .count{position:absolute;left:-6px;top:480px;display:flex;align-items:center;width:560px}
  .count__pill{background:var(--pill);border-radius:14px;padding:2px 12px;font-weight:700;font-size:20px;letter-spacing:1.5px;color:var(--ink)}
  .count__rule{flex:1;height:2px;background:linear-gradient(90deg,#e6e6e6,rgba(255,255,255,.4))}

  .panel-facts{position:absolute;left:860px;top:60px;width:200px;height:400px;background:var(--white);border:3px solid var(--rule);padding:10px 12px;font-size:11.5px;line-height:1.45;color:var(--ink)}
  .panel-facts h2{font-size:20px;font-weight:700;border-bottom:3px solid var(--rule);margin-bottom:8px;padding-bottom:2px}
  .panel-facts li{list-style:none;display:flex;justify-content:space-between;gap:6px;border-bottom:1px solid #bbb;padding:2px 0}
</style>
</head>
<body>

<section class="label label--warm">
  <div class="label__scene" role="img" aria-label="Photograph of sun rays breaking through clouds over the ocean at sunrise"></div>
  <p class="panel-story">Kel4 is a daily antioxidant blend that supports your regular routine. Take one capsule with water each morning. Store in a cool, dry place.</p>
  <div class="panel-front">
    <p class="kind">DIETARY<br>SUPPLEMENT</p>
    <div class="brand"><span class="brand__name">Kel4</span><span class="brand__mark"></span></div>
    <p class="tagline">Boost Your Regular<br>Skin Care Routine</p>
    <ul class="highlights">
      <li>Supports skin resilience</li>
      <li>Gradually builds skin comfort</li>
      <li>Promotes a more youthful appearance</li>
      <li>Provides antioxidant benefits</li>
    </ul>
    <p class="formula">DAILY USE ANTIOXIDANT<br>FOURMULA</p>
    <div class="count"><span class="count__pill">60 CAPSULES</span><span class="count__rule"></span></div>
  </div>
  <div class="panel-facts">
    <h2>Ingredients</h2>
    <ul>
      <li><span>Polypodium Extract</span><span>240mg</span></li>
      <li><span>Brelundix® MSM</span><span>200mg</span></li>
      <li><span>Grape Extract</span><span>150mg</span></li>
      <li><span>Pomegranate Extract</span><span>125mg</span></li>
      <li><span>Quistradex</span><span>35.5mg</span></li>
      <li><span>Lutein</span><span>7.5mg</span></li>
      <li><span>Organic Carrot Powder</span><span>13mg</span></li>
    </ul>
  </div>
</section>

<section class="label label--cool">
  <div class="label__scene" role="img" aria-label="Photograph of sun rays breaking through clouds over the ocean, in cooler violet tones"></div>
  <p class="panel-story">Kel4 is a daily antioxidant blend that supports your regular routine. Take one capsule with water each morning. Store in a cool, dry place.</p>
  <div class="panel-front">
    <p class="kind">DIETARY<br>SUPPLEMENT</p>
    <div class="brand"><span class="brand__name">Kel4</span><span class="brand__mark"></span></div>
    <p class="tagline">Boost Your Regular<br>Skin Care Routine</p>
    <ul class="highlights">
      <li>Supports skin resilience</li>
      <li>Gradually builds skin comfort</li>
      <li>Promotes a more youthful appearance</li>
      <li>Provides antioxidant benefits</li>
    </ul>
    <p class="formula">DAILY USE ANTIOXIDANT<br>FOURMULA</p>
    <div class="count"><span class="count__pill">60 CAPSULES</span><span class="count__rule"></span></div>
  </div>
  <div class="panel-facts">
    <h2>Ingredients</h2>
    <ul>
      <li><span>Polypodium Extract</span><span>240mg</span></li>
      <li><span>Brelundix® MSM</span><span>200mg</span></li>
      <li><span>Grape Extract</span><span>150mg</span></li>
      <li><span>Pomegranate Extract</span><span>125mg</span></li>
      <li><span>Quistradex</span><span>35.5mg</span></li>
      <li><span>Lutein</span><span>7.5mg</span></li>
      <li><span>Organic Carrot Powder</span><span>13mg</span></li>
    </ul>
  </div>
</section>

</body>
</html>
```